Northgate Print and Paper Business

Hi, I need template designs for stationary as listed below using my Logo as per attached file;
1) Business Card (double sided)
2) Letterhead
3) With Compliments Slip
4) Return Address Label (Stickers)

```html
<!DOCTYPE html>
<html lang="en">
<head>
<meta charset="utf-8">
<title>Northgate Print and Paper Business – Letterhead</title>
<link rel="stylesheet" href="https://fonts.googleapis.com/css2?family=Jost:wght@500;600&family=Open+Sans:wght@400&display=swap">
<style>
  :root {
    --backdrop: #d9d9d9;
    --paper: #ffffff;
    --magenta: #b5198f;
    --ink: #1a1a1a;
    --body-ink: #3a3a3a;
  }
  * { box-sizing: border-box; margin: 0; padding: 0; }
  html, body { width: 1200px; height: 1000px; overflow: hidden; }
  body { background: var(--backdrop); }
  .letterhead {
    position: absolute;
    left: 260px; top: 19px;
    width: 680px; height: 962px;
    background: var(--paper);
    overflow: hidden;
  }
  .edge-band {
    position: absolute;
    top: 0; right: 0;
    width: 18px; height: 100%;
    background: var(--magenta);
  }
  .brand {
    position: absolute;
    left: 62px; top: 92px;
    width: 160px;
    display: flex; align-items: flex-start; gap: 8px;
  }
  .brand-dot {
    flex: none;
    width: 14px; height: 14px; margin-top: 6px;
    border-radius: 50%;
    background: var(--magenta);
  }
  .brand-name {
    font-family: "Jost", sans-serif;
    font-weight: 600;
    font-size: 22px;
    line-height: 1.05;
    color: var(--ink);
  }
  .sender {
    position: absolute;
    left: 255px; top: 84px;
    font-family: "Jost", sans-serif;
    font-weight: 500;
    font-size: 9.5px;
    line-height: 1.32;
    color: var(--ink);
  }
  .sender-name { color: var(--magenta); font-weight: 600; font-size: 11px; }
  .sender-abn { margin-bottom: 10px; }
  .letter {
    position: absolute;
    left: 145px; top: 322px;
    width: 490px;
    font-family: "Open Sans", sans-serif;
    font-size: 12.5px;
    line-height: 20px;
    color: var(--body-ink);
  }
  .recipient { margin-bottom: 14px; }
  .salutation { margin-bottom: 16px; }
  .letter p.body-copy { text-align: justify; margin-bottom: 18px; }
  .sign-off { margin-top: 22px; }
</style>
</head>
<body>
  <main class="letterhead">
    <div class="brand">
      <span class="brand-dot"></span>
      <span class="brand-name">Northgate Print and Paper Business</span>
    </div>

    <address class="sender" style="font-style:normal">
      <div class="sender-name">Northgate Print and Paper Business</div>
      <div class="sender-abn">ABN 51824093176</div>
      <div>PO Box 518</div>
      <div>Northgate QLD 4013 Australia</div>
      <div>M: 0400 275 918</div>
      <div>E: hello@northgateprint.com.au</div>
      <div>W: northgateprintpaper.com.au</div>
    </address>

    <article class="letter">
      <div class="recipient">
        Helen Carter<br>42 Linden Ave<br>Easton MA
      </div>
      <p class="salutation">Dear Mrs Helen Carter,</p>
      <p class="body-copy">Lorem ipsum dolor sit amet, consectetur adipiscing elit. Integer aliquet diam eget mi rutrum consectetur et id orci. Praesent vitae felis vitae justo elementum tincidunt. Duis pharetra turpis semper dui elementum nec aliquet lectus pulvinar. Donec condimentum mattis diam, id congue risus congue a. Maecenas commodo, nisi a gravida condimentum, elit erat condimentum leo, in pellentesque elit erat id nisi. Pellentesque consequat faucibus dictum. Nam tincidunt viverra elit at hendrerit. Quisque eget purus tellus. Mauris mattis nunc nec nisi pulvinar consectetur.</p>
      <p class="body-copy">Nunc molestie iaculis orci, vitae consequat mi condimentum vitae. Etiam et tortor velit. Sed ac magna tellus. Curabitur erat purus, congue et faucibus sit amet, fringilla elementum odio. Sed pretium tincidunt mi, nec fermentum urna interdum sed. Maecenas commodo, nisi a gravida condimentum, elit erat condimentum leo, in pellentesque elit erat id nisi. Pellentesque consequat faucibus dictum. Nam tincidunt viverra elit at hendrerit. Nam et lectus turpis, quis cursus ipsum. Maecenas non nibh odio. Sed in laoreet justo.</p>
      <p class="body-copy">Aenean sed sem lacus. Vivamus auctor, sapien non aliquet ultrices, mauris turpis porttitor nisl, id rutrum velit erat non urna. Praesent eu augue eu ligula feugiat malesuada. Proin nec nibh erat. Sed et leo id leo volutpat viverra non ac mi. In quis dictum magna. Donec ut dui sed dui tristique dictum. Donec varius sapien sed turpis dictum a dignissim diam facilisis.</p>
      <p class="sign-off">Yours Sincerely<br>Daniel Whitmore</p>
    </article>

    <div class="edge-band"></div>
  </main>
</body>
</html>
```